Stump Grinding sidewalk sign

I have an A-frame sign that has a 24" x 36" flat area for a vinyl sign to be applied to. the sign can also be applied to sheet metal and then screwed to the A-frame sign.
I have included a few pictures of my logo, the A-frame, and my business card.

Target Market(s)

Tree and stump industry

Font styles to use
Decorative

Requirements
Must have
• I would like my company name , logo, slogan, and phone number on the sign. Along with "Fully Insured" and "free Estimates".
The sign is black, and I would like bright colors such as safety green and/or neon yellow. Or possibly a florescent red?
Nice to have
• Some sort of background to break up the blank "solidness"

```html
<!DOCTYPE html>
<html lang="en">
<head>
<meta charset="utf-8">
<title>Harlo's Stump Grinding – Sidewalk Sign</title>
<link rel="stylesheet" href="https://fonts.googleapis.com/css2?family=Oswald:wght@700&family=Josefin+Sans:wght@700&family=Montserrat:wght@600;800&display=swap">
<style>
  :root {
    --frame: #111111;
    --signal-yellow: #f9c20e;
    --bark-brown: #432812;
    --forest-green: #1f7a30;
    --safety-green: #8bc34a;
    --panel-black: #242222;
    --ink: #2a2a2a;
    --white: #ffffff;
    --gold: #e9b21c;
  }
  * { margin: 0; padding: 0; box-sizing: border-box; }
  html, body { width: 815px; height: 1200px; overflow: hidden; background: var(--frame); }
  .sign {
    position: relative;
    width: 815px; height: 1200px;
    background: var(--frame);
  }
  .sign-face {
    position: absolute;
    left: 14px; top: 14px;
    width: 782px; height: 1170px;
    overflow: hidden;
  }
  .backdrop { position: absolute; inset: 0; }
  .job-photo {
    position: absolute;
    left: 0; top: 442px;
    width: 782px; height: 232px;
    height: 372px;
    background: linear-gradient(160deg, #6f9a3c 0%, #a98a4a 35%, #c7a46a 55%, #7ea447 80%, #5f8c33 100%);
    clip-path: polygon(0 0, 782px 120px, 782px 372px, 0 232px);
  }
  .brand-name {
    position: absolute;
    left: 36px; top: 10px;
    font-family: "Oswald", sans-serif;
    font-weight: 700;
    color: var(--ink);
    line-height: 1;
  }
  .brand-name .title {
    display: block;
    font-size: 122px;
    letter-spacing: -1px;
  }
  .brand-name .subtitle {
    display: block;
    margin-top: -4px;
    margin-left: 8px;
    font-size: 50px;
    letter-spacing: 1px;
  }
  .brand-mark {
    position: absolute;
    left: 540px; top: 30px;
    width: 220px; height: 220px;
    border-radius: 50%;
    background: var(--bark-brown);
  }
  .headline {
    position: absolute;
    left: 54px; top: 272px;
    font-family: "Josefin Sans", sans-serif;
    font-weight: 700;
    color: var(--signal-yellow);
    line-height: 1;
    white-space: nowrap;
  }
  .headline .lead { display: block; font-size: 100px; }
  .headline .rest { display: block; font-size: 65px; margin-top: 4px; }
  .guarantee-seal {
    position: absolute;
    left: 101px; top: 634px;
    width: 192px; height: 192px;
  }
  .perks {
    position: absolute;
    left: 126px; top: 850px;
    list-style: none;
    font-family: "Montserrat", sans-serif;
    font-weight: 800;
    font-size: 58px;
    color: #111;
    line-height: 1;
  }
  .perks li {
    display: flex;
    align-items: center;
    height: 86px;
    white-space: nowrap;
  }
  .perks svg { width: 54px; height: 54px; margin-right: 22px; flex: none; }
  .contact {
    position: absolute;
    left: 128px; top: 1044px;
    display: flex;
    align-items: center;
  }
  .contact svg { width: 110px; height: 110px; flex: none; }
  .contact .phone-number {
    margin-left: 22px;
    font-family: "Montserrat", sans-serif;
    font-weight: 600;
    font-size: 66px;
    letter-spacing: -1px;
    color: var(--white);
    white-space: nowrap;
  }
</style>
</head>
<body>
<div class="sign">
  <div class="sign-face">
    <svg class="backdrop" width="782" height="1170" viewBox="0 0 782 1170">
      <rect class="band-brown" x="0" y="0" width="782" height="600" fill="var(--bark-brown)"/>
      <polygon class="band-yellow" points="0,0 782,0 782,274 0,202" fill="var(--signal-yellow)"/>
      <polygon class="stripe-forest" points="0,674 782,814 782,826 0,714" fill="var(--forest-green)"/>
      <polygon class="field-green" points="0,714 782,826 782,1170 0,1170" fill="var(--safety-green)"/>
      <polygon class="panel-contact" points="118,1026 782,1026 782,1170 0,1170 0,1146" fill="var(--panel-black)"/>
    </svg>

    <div class="job-photo" role="img" aria-label="Photo of an orange stump grinder on a lawn beside cut log rounds and a fresh tree stump"></div>

    <div class="brand-mark" aria-hidden="true"></div>
    <h1 class="brand-name">
      <span class="title">HARLO'S</span>
      <span class="subtitle">STUMP GRINDING</span>
    </h1>

    <h2 class="headline">
      <span class="lead">STUMP</span>
      <span class="rest">REMOVAL SERVICES</span>
    </h2>

    <svg class="guarantee-seal" viewBox="0 0 192 192" aria-hidden="true">
      <circle cx="96" cy="96" r="95" fill="var(--gold)"/>
      <circle cx="96" cy="96" r="66" fill="#1b1b1b"/>
      <circle cx="96" cy="96" r="40" fill="var(--gold)"/>
    </svg>

    <ul class="perks">
      <li>
        <svg viewBox="0 0 54 54" aria-hidden="true"><circle cx="27" cy="27" r="26" fill="#111"/><circle cx="27" cy="27" r="5" fill="var(--safety-green)"/></svg>
        FREE ESTIMATE
      </li>
      <li>
        <svg viewBox="0 0 54 54" aria-hidden="true"><circle cx="27" cy="27" r="26" fill="#111"/><circle cx="27" cy="27" r="5" fill="var(--safety-green)"/></svg>
        FULLY INSURED
      </li>
    </ul>

    <div class="contact">
      <svg viewBox="0 0 110 110" aria-hidden="true">
        <circle cx="55" cy="55" r="51" fill="none" stroke="var(--white)" stroke-width="4"/>
        <path d="M38 28c3-2 7-2 9 1l6 10c2 3 1 6-1 8l-4 3c3 7 8 12 15 16l3-4c2-2 5-3 8-1l10 6c3 2 3 6 1 9l-4 5c-3 3-8 4-13 2-19-8-32-22-39-41-2-5-1-10 2-13z" fill="var(--white)"/>
      </svg>
      <span class="phone-number">(555) 214 3860</span>
    </div>
  </div>
</div>
</body>
</html>
```